brolvix new business card design project

we need a new business card design. you can view info about us @ brolvix.example. i have attached an example of our previous card with our previous name that we no longer use. We really liked the design, colors etc. look below to see more info about this project. it asks for a limited number of words. please see our website for more info about our compnay.

Target Market(s)

law enforcement

Contact Information for Business Card

i have uploaded an example of what we used before that we liked.

Font styles to use
Serif

```html
<!DOCTYPE html>
<html lang="en">
<head>
<meta charset="utf-8">
<title>Brolvix Business Card</title>
<link href="https://fonts.googleapis.com/css2?family=Open+Sans:wght@300;400;600&display=swap" rel="stylesheet">
<style>
  :root {
    --stage: #5b5049;
    --navy: #1b2f66;
    --blue-deep: #0f2a78;
    --blue-mid: #1b55b8;
    --blue-glow: #2d74d6;
    --white: #ffffff;
    --ink-soft: #4a4f5c;
    --rule: #8a9abb;
  }
  * { box-sizing: border-box; margin: 0; padding: 0; }
  html, body { width: 1200px; height: 1200px; overflow: hidden; }
  body {
    background: var(--stage);
    font-family: "Open Sans", Arial, sans-serif;
    position: relative;
  }
  .card {
    position: absolute;
    width: 760px;
    height: 434px;
    border-radius: 4px;
    overflow: hidden;
    box-shadow: 0 14px 30px rgba(0,0,0,0.35);
  }
  /* Front */
  .card-front {
    left: 70px; top: 110px;
    background: radial-gradient(ellipse at 45% 20%, var(--blue-glow) 0%, var(--blue-mid) 35%, var(--blue-deep) 100%);
    color: var(--white);
  }
  .front-artwork {
    position: absolute;
    right: -60px; top: 20px;
    width: 360px; height: 360px;
    border-radius: 50%;
    background: radial-gradient(circle at 40% 40%, rgba(120,190,255,0.55) 0%, rgba(45,110,220,0.45) 45%, rgba(15,42,120,0) 72%);
  }
  .front-brand {
    position: absolute;
    left: 70px; top: 170px;
    font-weight: 300;
    font-size: 70px;
    letter-spacing: 6px;
    line-height: 1;
  }
  .front-address {
    position: absolute;
    left: 74px; top: 262px;
    font-size: 22px;
    font-weight: 400;
    line-height: 1.5;
    letter-spacing: 0.5px;
  }
  /* Back */
  .card-back {
    left: 370px; top: 656px;
    background: var(--white);
  }
  .back-brand-block {
    position: absolute;
    left: 60px; top: 0; height: 100%;
    display: flex; align-items: center;
  }
  .back-brand {
    font-weight: 300;
    font-size: 64px;
    letter-spacing: 5px;
    color: var(--navy);
    line-height: 1;
  }
  .divider {
    position: absolute;
    left: 410px; top: 120px;
    width: 1.5px; height: 190px;
    background: var(--rule);
  }
  .person {
    position: absolute;
    left: 438px; top: 120px;
    color: var(--navy);
  }
  .person-name {
    font-weight: 600;
    font-size: 28px;
    letter-spacing: 0.5px;
    line-height: 1.1;
  }
  .person-title {
    font-size: 19px;
    color: var(--ink-soft);
    margin-top: 4px;
  }
  .contact-list {
    list-style: none;
    margin-top: 22px;
  }
  .contact-item {
    display: flex; align-items: center;
    gap: 12px;
    font-size: 19px;
    color: var(--ink-soft);
    line-height: 1.55;
  }
  .contact-icon {
    width: 20px; height: 20px;
    flex: none;
  }
</style>
</head>
<body>
  <section class="card card-front" aria-label="Card front">
    <div class="front-artwork" role="img" aria-label="Glowing blue network globe illustration"></div>
    <div class="front-brand">BROLVIX</div>
    <address class="front-address" style="font-style: normal;">
      1420 Harlow Lane<br>
      Fairbrook, TX 75001
    </address>
  </section>

  <section class="card card-back" aria-label="Card back">
    <div class="back-brand-block"><div class="back-brand">BROLVIX</div></div>
    <div class="divider"></div>
    <div class="person">
      <div class="person-name">DANA MERCER</div>
      <div class="person-title">Creative Designer</div>
      <ul class="contact-list">
        <li class="contact-item">
          <svg class="contact-icon" viewBox="0 0 20 20" aria-hidden="true">
            <rect width="20" height="20" rx="4" fill="#1b2f66"/>
            <path d="M5 8c0-2 2-3 5-3s5 1 5 3l-2 1-1-2H8L7 9z M6 10h8l1 5H5z" fill="#fff"/>
            <circle cx="10" cy="12.5" r="1.3" fill="#1b2f66"/>
          </svg>
          555.014.2290
        </li>
        <li class="contact-item">
          <svg class="contact-icon" viewBox="0 0 20 20" aria-hidden="true">
            <rect width="20" height="20" rx="4" fill="#1b2f66"/>
            <circle cx="10" cy="10" r="5.5" fill="none" stroke="#fff" stroke-width="1.2"/>
            <ellipse cx="10" cy="10" rx="2.4" ry="5.5" fill="none" stroke="#fff" stroke-width="1"/>
            <path d="M4.5 10h11M5.5 7h9M5.5 13h9" stroke="#fff" stroke-width="0.9"/>
          </svg>
          www.brolvix.example
        </li>
        <li class="contact-item">
          <svg class="contact-icon" viewBox="0 0 20 20" aria-hidden="true">
            <rect width="20" height="20" rx="4" fill="#1b2f66"/>
            <rect x="4.5" y="6" width="11" height="8" fill="#fff"/>
            <path d="M4.5 6l5.5 4.5L15.5 6" fill="none" stroke="#1b2f66" stroke-width="1.1"/>
          </svg>
          info@brolvix.example
        </li>
      </ul>
    </div>
  </section>
</body>
</html>
```